Hallvard
Veneer Technology
Hallvard - Agriculture
Creative Brief
Agriculture
http://hallvard-veneertechnology.example
We have 4 different product lines.
1. Stone-Veneer
2.Sonic-Paneltrim
3.Plexard
4.Moravelt
We do not installl any products. We just distribute them to architects, companies, builders, ect.
The stone can be made for any products. From laptops, countertops, "wall paper", notebooks, smart car, sinks, ect.
Dislikes: -it's hard to see what our company is -appearance -professionalism -pictures -it's not appealing
Nature
Gray, white and blacks
Blues
Red (Nothing too bright!)
below header
http://www.brevicott.example
http://www.folmaneq.example/
http://4plank.example

```html
<!DOCTYPE html>
<html lang="en">
<head>
<meta charset="utf-8">
<title>Hallvard Veneer Technology</title>
<link href="https://fonts.googleapis.com/css2?family=Arimo:wght@400;700&display=swap" rel="stylesheet">
<style>
:root{
  --red:#c8202a;
  --ink:#111;
  --grey-dark:#3a3a3a;
  --grey-mid:#8a8a8a;
  --grey-light:#e4e4e4;
  --white:#fff;
  --text-soft:#666;
}
*{box-sizing:border-box;margin:0;padding:0}
html,body{width:1200px;height:1014px;overflow:hidden}
body{position:relative;font-family:"Arimo",Arial,sans-serif;background:linear-gradient(#fdfdfd 0,#e9e9e9 14%,#dadada 60%,#cfcfcf 100%);color:var(--ink)}
.abs{position:absolute}
.brand{left:104px;top:40px;font-size:40px;font-weight:400;color:var(--grey-dark);line-height:1}
.tagline{left:104px;top:96px;font-size:27px;color:var(--ink)}
.tagline b{font-weight:700}
.search{left:753px;top:99px;display:flex;gap:8px}
.search-field{width:219px;height:20px;background:var(--white);border:1px solid #bbb}
.search-btn{width:88px;height:20px;background:var(--grey-dark);color:var(--white);font-size:13px;text-align:center;line-height:20px}
.nav{left:99px;top:129px;width:1008px;height:68px;background:linear-gradient(#f4f4f4,#c9c9c9);border-radius:3px}
.nav-item{position:absolute;top:22px;font-size:21px;color:var(--ink);transform:translateX(-50%);white-space:nowrap}
.nav-active{position:absolute;left:0;top:0;width:153px;height:68px;background:linear-gradient(#9a9a9a,#6d6d6d);border-radius:3px 0 0 3px}
.hero{left:99px;top:214px;width:1008px;height:252px;border-radius:4px;background:linear-gradient(100deg,#e6dcd2 0,#cfc3b6 30%,#8e2a25 55%,#b9312c 75%,#d9d2cb 100%)}
.card{top:485px;width:238px;height:233px;background:linear-gradient(#fff,#eee);border-radius:6px;box-shadow:0 1px 3px rgba(0,0,0,.25)}
.card h2{margin-top:14px;text-align:center;font-size:22px;font-weight:400;color:var(--red)}
.card-img{width:150px;height:108px;margin:8px auto 0}
.card p{margin:9px 12px 0;font-size:11.5px;line-height:13px;color:var(--text-soft);text-align:left}
.read-more{position:absolute;right:10px;bottom:8px;background:var(--grey-dark);color:var(--white);font-size:11px;padding:2px 6px}
.panel{left:99px;top:729px;width:674px;height:227px;border-radius:6px;background:linear-gradient(#5e5e5e,#8d8d8d 60%,#7a7a7a);box-shadow:0 1px 3px rgba(0,0,0,.3)}
.panel h3{position:absolute;top:16px;font-size:28px;font-weight:400;color:var(--white)}
.panel .rule{position:absolute;top:54px;height:1px;width:200px;background:#bbb}
.panel ul{position:absolute;top:66px;list-style:none}
.panel li{height:30px;font-size:13px;color:var(--white);display:flex;align-items:center;gap:14px}
.panel li::before{content:"";width:9px;height:9px;border-radius:50%;border:2px solid #ddd;box-sizing:border-box}
.panel li.current::before{background:#eee}
.quote{left:792px;top:729px;width:312px;height:227px;border-radius:6px;background:linear-gradient(#f8f8f8,#e3e3e3);box-shadow:0 1px 3px rgba(0,0,0,.3);overflow:hidden}
.quote-head{height:47px;background:linear-gradient(#3a3a3a,#111);color:var(--white);font-size:26px;padding:9px 10px}
.quote-row{position:absolute;left:4px;font-size:21px;display:flex;align-items:center}
.quote-row span{width:94px}
.quote-field{width:190px;height:22px;background:var(--white);border:1px solid #bbb}
.submit{position:absolute;left:216px;top:189px;width:77px;height:22px;border-radius:3px;background:var(--grey-dark);color:var(--white);font-size:14px;text-align:center;line-height:22px}
.footer{left:0;top:964px;width:1200px;height:50px;background:linear-gradient(#bdbdbd,#e6e6e6);text-align:center;font-size:14px;line-height:50px;color:var(--ink)}
</style>
</head>
<body>
<header>
  <div class="abs brand">Hallvard</div>
  <div class="abs tagline"><b>veneer technology</b>....Designed By Nature</div>
  <div class="abs search"><div class="search-field"></div><div class="search-btn">Search</div></div>
  <nav class="abs nav">
    <div class="nav-active"></div>
    <span class="nav-item" style="left:76px">Home</span>
    <span class="nav-item" style="left:246px">About Us</span>
    <span class="nav-item" style="left:416px">Services</span>
    <span class="nav-item" style="left:586px">Products</span>
    <span class="nav-item" style="left:756px">Contact Us</span>
  </nav>
</header>

<div class="abs hero" role="img" aria-label="Modern living room with red wall, white furniture and shelving"></div>

<section>
  <article class="abs card" style="left:101px">
    <h2>Stone-Veneer</h2>
    <div class="card-img" role="img" aria-label="Stone veneer sheets" style="background:linear-gradient(135deg,#9b8f80,#5e4a3c)"></div>
    <p>It is a long established fact that a reader will be distracted by the readable content of a page when looking at its layout</p>
    <span class="read-more">READ MORE</span>
  </article>
  <article class="abs card" style="left:359px">
    <h2>Sonic-Paneltrim</h2>
    <div class="card-img" role="img" aria-label="Wooden slatted acoustic panel" style="background:linear-gradient(135deg,#b47a3e,#6b4020)"></div>
    <p>It is a long established fact that a reader will be distracted by the readable content of a page when looking at its layout</p>
    <span class="read-more">READ MORE</span>
  </article>
  <article class="abs card" style="left:606px">
    <h2>Plexard</h2>
    <div class="card-img" role="img" aria-label="Interior with wall panels and windows" style="background:linear-gradient(135deg,#9fb7cf,#6a7a5a)"></div>
    <p>It is a long established fact that a reader will be distracted by the readable content of a page when looking at its layout</p>
    <span class="read-more">READ MORE</span>
  </article>
  <article class="abs card" style="left:860px">
    <h2>Moravelt</h2>
    <div class="card-img" role="img" aria-label="Light wood acoustic slats" style="background:linear-gradient(135deg,#e0b77a,#a2733a)"></div>
    <p>It is a long established fact that a reader will be distracted by the readable content of a page when looking at its layout</p>
    <span class="read-more">READ MORE</span>
  </article>
</section>

<section class="abs panel">
  <h3 style="left:24px">Navigation</h3>
  <div class="rule" style="left:24px"></div>
  <ul style="left:14px">
    <li>Home</li><li>News</li><li>Products</li><li>Corporate Social Responsibility</li><li>Contact Us</li>
  </ul>
  <h3 style="left:394px">Products</h3>
  <div class="rule" style="left:394px"></div>
  <ul style="left:364px">
    <li class="current">Stone-Veneer</li><li>Sonic-Paneltrim</li><li>Plexard</li><li>Moravelt</li>
  </ul>
</section>

<section class="abs quote">
  <div class="quote-head">Get A Quote</div>
  <div class="quote-row" style="top:55px"><span>Name</span><div class="quote-field"></div></div>
  <div class="quote-row" style="top:93px"><span>Phone</span><div class="quote-field"></div></div>
  <div class="quote-row" style="top:137px"><span>Email</span><div class="quote-field"></div></div>
  <div class="submit">Submit</div>
</section>

<footer class="abs footer">Copyright © Hallvard Veneer Technology,2010-2011</footer>
</body>
</html>
```